Brochure design - Ventoro Rideshare community

We need a print ready brochure to tell drivers about the Ventoro community and the benefits of being a driver. We offer a alternative product to zappo and give drivers the ability to build their own customer base and build passive income. see design brief. check out our website www.ventoro-example.travel put in some good pics. Wanting a A4 Double sided brochure

Target Market(s)

Rideshare Drivers

Industry/Entity Type

Community

Font styles to use
Serif

Colors
00a990

Requirements
Must have
• clean design look. not too busy

```html
<!DOCTYPE html>
<html lang="en">
<head>
<meta charset="utf-8">
<title>Ventoro Rideshare – Driver Brochure</title>
<link rel="stylesheet" href="https://fonts.googleapis.com/css2?family=Lato:wght@300;400;700;900&display=swap">
<style>
  :root {
    --backdrop: #d6d7d9;
    --paper: #f4f4f6;
    --paper-shade: #c9cacf;
    --ink: #1a1a1c;
    --ink-soft: #3b3b40;
    --dark: #2a2a2e;
    --dark-deep: #151517;
    --on-dark: #e8e8ea;
    --band-blue: #4a7ac8;
    --band-green: #6ab04c;
    --band-green-deep: #3f8a3e;
    --band-orange: #d07a3c;
    --band-redorange: #d2483a;
    --band-red: #c8322f;
    --band-tip: #c02a2a;
    --accent-blue: #4a7ac8;
  }
  * { box-sizing: border-box; margin: 0; padding: 0; }
  html, body { width: 801px; height: 1200px; overflow: hidden; background: var(--backdrop); }
  body { font-family: "Lato", Arial, sans-serif; color: var(--ink); }
  .canvas { position: relative; width: 801px; height: 1200px; overflow: hidden; background: var(--backdrop); }

  .spread { position: absolute; left: 40px; width: 720px; height: 510px; display: flex; box-shadow: 0 6px 18px rgba(0,0,0,.25); }
  .spread--outer { top: 40px; }
  .spread--inner { top: 640px; }
  .page { position: relative; width: 360px; height: 100%; overflow: hidden; }

  /* Outer spread: back cover */
  .page--back { background: linear-gradient(180deg, #f2f2f4 0%, #d9dade 48%, var(--dark) 62%, var(--dark-deep) 100%); }
  .back-swoosh { position: absolute; left: 0; top: 280px; width: 360px; height: 70px; }
  .back-title { position: absolute; top: 36px; left: 0; right: 0; text-align: center; font-size: 21px; font-weight: 700; line-height: 1.15; }
  .back-car { position: absolute; top: 98px; left: 34px; width: 292px; height: 120px; border-radius: 40px 60px 18px 18px; background: linear-gradient(180deg, #3a3a40, #121214); }
  .service-table { position: absolute; top: 232px; left: 60px; width: 240px; border-collapse: collapse; font-size: 10.5px; background: #fff; }
  .service-table th { background: var(--ink); color: #fff; font-weight: 700; text-align: left; padding: 3px 6px; }
  .service-table td { padding: 3px 6px; border: 1px solid var(--ink); font-weight: 700; }
  .back-copy { position: absolute; top: 356px; left: 0; right: 0; text-align: center; color: var(--on-dark); font-size: 11.5px; line-height: 1.35; font-weight: 300; }
  .back-copy p + p { margin-top: 12px; }
  .back-web { position: absolute; bottom: 40px; left: 0; right: 0; text-align: center; color: var(--on-dark); font-size: 17px; font-weight: 300; }

  /* Outer spread: front cover */
  .page--front { background: linear-gradient(180deg, #f5f5f7 0%, #dcdde1 45%, var(--dark) 70%, var(--dark-deep) 100%); }
  .brand-name { position: absolute; top: 44px; left: 0; right: 0; text-align: center; font-size: 30px; font-weight: 700; line-height: 1; color: var(--ink); }
  .front-car { position: absolute; top: 130px; left: 40px; width: 320px; height: 170px; border-radius: 90px 0 0 40px; background: linear-gradient(160deg, #e6e7ea 0%, #a9abb1 55%, #5a5b60 100%); }
  .front-swoosh { position: absolute; left: 0; top: 288px; width: 360px; height: 40px; }
  .front-call { position: absolute; top: 392px; left: 0; right: 0; text-align: center; color: var(--on-dark); font-size: 21px; font-weight: 300; line-height: 1.25; }

  /* Inner spread */
  .page--inner-left { background: linear-gradient(90deg, var(--paper) 80%, var(--paper-shade) 100%); padding: 22px 20px 0 24px; }
  .page--inner-right { background: linear-gradient(90deg, var(--paper-shade) 0%, var(--paper) 14%); }
  .page-foot { position: absolute; left: 0; right: 0; bottom: 0; height: 14px; background: var(--dark-deep); }

  .benefits { list-style: none; }
  .benefit { position: relative; padding-left: 12px; margin-bottom: 9px; }
  .benefit::before { content: ""; position: absolute; left: 0; top: 5px; width: 5px; height: 5px; border-radius: 50%; background: var(--ink); }
  .benefit h3 { font-size: 10.5px; font-weight: 900; font-style: italic; margin-bottom: 2px; }
  .benefit p { font-size: 8.5px; line-height: 1.3; color: var(--ink-soft); }

  .dist-title { position: absolute; top: 26px; left: 34px; font-size: 17px; font-weight: 700; }
  .dist-chart { position: absolute; top: 60px; left: 30px; width: 270px; height: 240px; }
  .dist-chart text { font-family: "Lato", Arial, sans-serif; font-size: 11px; font-weight: 700; fill: #111; }
  .dist-chart .booking { fill: var(--accent-blue); font-size: 11px; }
  .people { position: absolute; top: 210px; right: 24px; width: 64px; height: 110px; background: linear-gradient(180deg, #777, #4a4a4a); clip-path: polygon(50% 0, 100% 100%, 0 100%); }
  .refer { position: absolute; top: 332px; left: 30px; right: 24px; text-align: right; font-size: 17px; font-weight: 700; line-height: 1.2; }
  .how { position: absolute; top: 392px; left: 30px; right: 22px; }
  .how h4 { font-size: 10.5px; font-weight: 900; line-height: 1.3; }
  .how ol { margin-top: 4px; padding-left: 14px; font-size: 8.5px; line-height: 1.35; color: var(--ink-soft); }
</style>
</head>
<body>
<main class="canvas">

  <section class="spread spread--outer" aria-label="Brochure outer spread">
    <article class="page page--back">
      <h2 class="back-title">We offer clients a range<br>of services</h2>
      <div class="back-car" role="img" aria-label="Photo of a black executive sedan"></div>
      <svg class="back-swoosh" viewBox="0 0 360 70" preserveAspectRatio="none" aria-hidden="true">
        <path d="M0 62 Q120 8 360 26 L360 32 Q120 18 0 70 Z" fill="#ffffff" opacity=".55"/>
      </svg>
      <table class="service-table">
        <thead><tr><th>Ventoro</th><th>Zappo</th></tr></thead>
        <tbody>
          <tr><td>Ventoro Business</td><td>Zappo Black</td></tr>
          <tr><td>Ventoro Premium Economy</td><td>Zappo Select</td></tr>
          <tr><td>Ventoro Ride</td><td>Zappo X</td></tr>
        </tbody>
      </table>
      <div class="back-copy">
        <p>It is easy to join. Sign up online an upload<br>your compliance documents.</p>
        <p>$149 Special offer $49 activation fee<br>Monthly access fee only $19.95</p>
      </div>
      <p class="back-web">www.ventoro-example.travel</p>
    </article>

    <article class="page page--front">
      <h1 class="brand-name">Ventoro</h1>
      <div class="front-car" role="img" aria-label="Close-up photo of a silver car front and wheel"></div>
      <svg class="front-swoosh" viewBox="0 0 360 40" preserveAspectRatio="none" aria-hidden="true">
        <path d="M0 30 Q180 -4 360 20 L360 26 Q180 6 0 40 Z" fill="#ffffff" opacity=".6"/>
      </svg>
      <p class="front-call">Be a part of the Ventoro<br>Community......</p>
    </article>
  </section>

  <section class="spread spread--inner" aria-label="Brochure inner spread">
    <article class="page page--inner-left">
      <ul class="benefits">
        <li class="benefit"><h3>Earn Commission $$ for referring customers</h3>
          <p>Being a part of the Ventoro community gives you the ability to earn passive income by simply referring customers to your network. You earn commission on each journey they take.</p></li>
        <li class="benefit"><h3>Join the Ventoro Community Today</h3>
          <p>Be part of the travel revolution. Sign up today to join the community and receive booking notifications. Get access to view jobs in your area.</p></li>
        <li class="benefit"><h3>Build your own client base with Ventoro</h3>
          <p>With Ventoro you can build up your own client base. After each journey the client can select you as their preferred driver, giving you first access to their bookings.</p></li>
        <li class="benefit"><h3>Minimum fare $29</h3>
          <p>We understand that you are running a business, so we have set a minimum fare of $29. No more small fares that do not cover your costs.</p></li>
        <li class="benefit"><h3>We pay you for referring customers</h3>
          <p>Have you ever been asked by a customer if they can book you? Refer them to Ventoro and earn commission on every booking they make.</p></li>
        <li class="benefit"><h3>Pre booked set price</h3>
          <p>At Ventoro we believe in being upfront. The price you see on the app is the amount you receive. You decide if the job is right for you.</p></li>
        <li class="benefit"><h3>Preferred driver – have 1st option to complete your clients transfer</h3>
          <p>If you are a preferred driver for a client you will receive first option to accept the transfer. If you are not available the client is still looked after.</p></li>
      </ul>
      <div class="page-foot"></div>
    </article>

    <article class="page page--inner-right">
      <h2 class="dist-title">How we distribute jobs</h2>
      <svg class="dist-chart" viewBox="0 0 270 240" aria-label="Job distribution funnel">
        <defs>
          <clipPath id="funnel-shape"><polygon points="0,22 270,22 20,240"/></clipPath>
        </defs>
        <text class="booking" x="4" y="14">Booking Created</text>
        <g clip-path="url(#funnel-shape)">
          <rect x="0" y="22" width="270" height="30" fill="var(--band-blue)"/>
          <rect x="0" y="52" width="270" height="30" fill="var(--band-green)"/>
          <rect x="0" y="82" width="270" height="30" fill="var(--band-green-deep)"/>
          <rect x="0" y="112" width="270" height="28" fill="var(--band-orange)"/>
          <rect x="0" y="140" width="270" height="28" fill="var(--band-redorange)"/>
          <rect x="0" y="168" width="270" height="28" fill="var(--band-red)"/>
          <rect x="0" y="196" width="270" height="44" fill="var(--band-tip)"/>
        </g>
        <text x="8" y="41">Perferred Driver - 1 Hrs</text>
        <text x="8" y="71">Exclusive Suburb - 2 Hrs</text>
        <text x="8" y="101">Shared Suburb - 2 Hrs</text>
        <text x="10" y="130">Priority Points</text>
        <text x="12" y="158">Standard</text>
        <text x="14" y="186">Distribution</text>
      </svg>
      <div class="people" role="img" aria-label="Pyramid of referred people figures"></div>
      <p class="refer">Refer your way to<br>$200 / wk passive income.</p>
      <div class="how">
        <h4>Earning commission as part of the community is easy.<br>Here's how it works.</h4>
        <ol>
          <li>Have a chat with someone who enjoyed their ride.</li>
          <li>Refer 4 people a week who each travel once with the community.</li>
          <li>In just 4 months you will be earning $200 commission per week.</li>
        </ol>
      </div>
      <div class="page-foot"></div>
    </article>
  </section>

</main>
</body>
</html>
```